High-end construction company needs a business card design

We need a modern looking business card that draws people in, is memorable and looks so good people will want to sick it on their fridges.
On the first side what is needed are:
Logo
My name - Tomas Verbelk
Title - Managing Director
Website - www.kravel.co.uk
Email - tomas@kravel.co.uk
Telephone - 020 5194 6381
Mobile - 07845319027
On the back side was is needed is a list of all the services we provide:
-Kitchen Renovations
-Bathroom Renovations
-House Renovations
-Garage Conversions
-Extensions
-Loft Conversions
-Conservatories
-Carpentry
-Tiling
-Electrical
-Plumbing & Heating
-Bricklaying
-Landscaping
-Decorating
-Plastering
We would like the colours to be the same shades as on the logo with grey or black for the words.
Target Market(s)
Anyone who needs building work done
Contact Information for Business Card
This business card is for a construction company which strives to deliver excellent service and quality.
The look and feel of the card should represent this.
Requirements
Must have
- On the first side what is needed are:
Logo
My name - Tomas Verbelk
Title - Managing Director
Website - www.kravel.co.uk
Email - tomas@kravel.co.uk
Telephone - 020 5194 6381
Mobile - 07845319027
Nice to have
- Cool looking features

```html
<!DOCTYPE html>
<html lang="en">
<head>
<meta charset="utf-8">
<title>Kravel Construction – Business Card</title>
<link rel="stylesheet" href="https://fonts.googleapis.com/css2?family=Mulish:wght@400;600;800&display=swap">
<style>
  :root {
    --brand-green: #4ed41c;
    --card-white: #ffffff;
    --card-charcoal: #464646;
    --text-grey: #3a3a3a;
    --text-light: #f2f2f2;
    --backdrop: #e8efe8;
  }
  * { box-sizing: border-box; margin: 0; padding: 0; }
  html, body { width: 1200px; height: 770px; overflow: hidden; }
  body {
    background: var(--backdrop);
    font-family: "Mulish", Arial, sans-serif;
    position: relative;
  }
  .card {
    position: absolute;
    top: 235px;
    width: 500px;
    height: 300px;
    border-radius: 18px;
    box-shadow: 0 10px 28px rgba(0,0,0,.14);
    overflow: hidden;
  }
  .card--front { left: 80px; background: var(--card-white); }
  .card--back { left: 620px; background: var(--card-charcoal); }

  .website {
    position: absolute; left: 36px; top: 104px;
    color: var(--brand-green); font-size: 13px; font-weight: 600;
  }
  .brand-name {
    position: absolute; right: 36px; top: 34px;
    color: var(--brand-green); font-weight: 800; text-align: center;
    line-height: 1;
  }
  .brand-name__main { display: block; font-size: 40px; letter-spacing: 1px; }
  .brand-name__sub { display: block; font-size: 10.5px; letter-spacing: 2.2px; margin-top: 4px; }

  .phones {
    position: absolute; right: 36px; top: 166px;
    font-size: 13px; color: var(--text-grey); display: flex; gap: 16px;
    white-space: nowrap;
  }
  .label { color: var(--brand-green); }
  .person { position: absolute; left: 90px; top: 196px; }
  .person__name { color: var(--brand-green); font-size: 21px; font-weight: 800; }
  .person__title { color: var(--text-grey); font-size: 14px; margin-top: 2px; padding-left: 10px; }
  .email {
    position: absolute; left: 110px; top: 252px;
    font-size: 13px; color: var(--text-grey);
  }

  .services { position: absolute; left: 36px; top: 146px; right: 20px; }
  .services__heading {
    color: var(--brand-green); font-size: 12.5px; font-weight: 600; margin-bottom: 8px;
  }
  .services__list {
    list-style: none; color: var(--text-light);
    font-size: 12px; line-height: 1.6; white-space: nowrap;
  }
  .sep { color: var(--brand-green); padding: 0 2px; }
</style>
</head>
<body>
  <section class="card card--front" aria-label="Business card front">
    <div class="brand-name">
      <span class="brand-name__main">KRAVEL</span>
      <span class="brand-name__sub">CONSTRUCTION LTD</span>
    </div>
    <p class="website">www.kravel.co.uk</p>
    <p class="phones">
      <span><span class="label">m /</span> 078-4531 9027</span>
      <span><span class="label">t /</span> 020 5194 6381</span>
    </p>
    <div class="person">
      <h1 class="person__name">Tomas Verbelk</h1>
      <p class="person__title">Managing Director</p>
    </div>
    <p class="email"><span class="label">e /</span> tomas@kravel.co.uk</p>
  </section>

  <section class="card card--back" aria-label="Business card back">
    <div class="services">
      <h2 class="services__heading">/ our services</h2>
      <ul class="services__list">
        <li>Kitchen Renovations <span class="sep">/</span> Bathroom Renovations <span class="sep">/</span> House Renovations <span class="sep">/</span></li>
        <li>Garage Conversions <span class="sep">/</span> Extensions <span class="sep">/</span> Loft Conversions <span class="sep">/</span> Conservatories <span class="sep">/</span></li>
        <li>Carpentry <span class="sep">/</span> Tiling <span class="sep">/</span> Electrical <span class="sep">/</span> Plumbing &amp; Heating <span class="sep">/</span> Bricklaying <span class="sep">/</span></li>
        <li>Landscaping <span class="sep">/</span> Decorating <span class="sep">/</span> Plastering</li>
      </ul>
    </div>
  </section>
</body>
</html>
```